Energy Company needs a Business Card Design

We need a business card design for a new company based in Singapore called Solvira Energy. Solvira Energy is a producer of renewable energies largely for the biofuels market. Sourced entirely from sustainable resources, Solvira Energy aims to be a fully integrated oil company operating in 100% sustainable way. We would like to see designs that use the same colours as the attached file.

Industry/Entity Type

Business

```html
<!DOCTYPE html>
<html lang="en">
<head>
<meta charset="UTF-8">
<title>Solvira Energy – Business Card</title>
<link rel="stylesheet" href="https://fonts.googleapis.com/css2?family=Exo+2:wght@500&display=swap">
<style>
  :root {
    --backdrop: #3a3a3c;
    --card-light: #e9e9ea;
    --leaf-green: #82c341;
    --lime-green: #b3d335;
    --brand-grey: #939598;
    --white: #ffffff;
  }
  * { margin: 0; padding: 0; box-sizing: border-box; }
  html, body {
    width: 1200px;
    height: 1000px;
    overflow: hidden;
    background: var(--backdrop);
    font-family: "Exo 2", sans-serif;
  }
  .canvas { position: relative; width: 1200px; height: 1000px; }

  .card {
    position: absolute;
    overflow: hidden;
    box-shadow: 0 4px 10px rgba(0, 0, 0, 0.45);
  }

  /* Front */
  .card-front {
    left: 292px; top: 100px;
    width: 612px; height: 388px;
    background: var(--card-light);
  }
  .card-front .corner-shapes { position: absolute; inset: 0; }
  .corner-top { fill: var(--leaf-green); }
  .corner-bottom { fill: var(--lime-green); }
  .front-name {
    position: absolute;
    left: 110px; top: 158px;
    width: 400px;
    text-align: center;
    font-size: 54px;
    font-weight: 500;
    line-height: 1;
    letter-spacing: 1px;
    color: var(--brand-grey);
    white-space: nowrap;
  }

  /* Back */
  .card-back {
    left: 292px; top: 513px;
    width: 616px; height: 387px;
    background: var(--leaf-green);
  }
  .back-name {
    position: absolute;
    left: 46px; top: 150px;
    width: 172px;
    text-align: center;
    font-size: 36px;
    font-weight: 500;
    line-height: 1.1;
    color: var(--white);
  }
  .divider {
    position: absolute;
    left: 234px; top: 85px;
    width: 4px; height: 227px;
    background: var(--white);
  }
  .contact-icons {
    position: absolute;
    left: 264px; top: 88px;
    list-style: none;
  }
  .contact-icons li {
    width: 30px; height: 30px;
    margin-bottom: 34px;
  }
  .contact-icons svg { width: 30px; height: 30px; fill: var(--white); }
</style>
</head>
<body>
<main class="canvas">
  <section class="card card-front" aria-label="Card front">
    <svg class="corner-shapes" width="612" height="388" viewBox="0 0 612 388" aria-hidden="true">
      <circle class="corner-top" cx="718" cy="-110" r="327"/>
      <circle class="corner-bottom" cx="-32" cy="460" r="270"/>
    </svg>
    <h1 class="front-name">Solvira Energy</h1>
  </section>

  <section class="card card-back" aria-label="Card back">
    <p class="back-name">Solvira<br>Energy</p>
    <span class="divider"></span>
    <ul class="contact-icons">
      <li aria-label="Address">
        <svg viewBox="0 0 24 24"><path d="M12 3 2 12h3v8h5v-5h4v5h5v-8h3z"/></svg>
      </li>
      <li aria-label="Phone">
        <svg viewBox="0 0 24 24"><path d="M6.6 10.8a15 15 0 0 0 6.6 6.6l2.2-2.2c.3-.3.7-.4 1-.2 1.1.4 2.3.6 3.6.6.6 0 1 .4 1 1V20c0 .6-.4 1-1 1A17 17 0 0 1 3 4c0-.6.4-1 1-1h3.5c.6 0 1 .4 1 1 0 1.3.2 2.5.6 3.6.1.3 0 .7-.2 1z"/></svg>
      </li>
      <li aria-label="Website">
        <svg viewBox="0 0 24 24" stroke="#ffffff" stroke-width="1.8" style="fill:none"><circle cx="12" cy="12" r="9.5"/><ellipse cx="12" cy="12" rx="4.5" ry="9.5"/><path d="M2.5 12h19M4 7h16M4 17h16M12 2.5v19"/></svg>
      </li>
      <li aria-label="Email">
        <svg viewBox="0 0 24 24"><path d="M2 5h20v14H2z"/><path d="M2 5l10 8 10-8" fill="none" stroke="#82c341" stroke-width="1.5"/></svg>
      </li>
    </ul>
  </section>
</main>
</body>
</html>
```